An e-flyer for an exotic car and fine wine club.

This is the first meeting of Birchwell Motor Society and includes several businesses. Their logos should be featured at the bottom. It should be sleek, elegant and simple featuring a photo of an Corvane Lestrel R7 as well as my logo (I will provide photos). The flyer needs to look professional and appeal to billionaires.
The text should read:
Birchwell Motor society presents
Fast Cars and Fine Wine (but not while driving)
Hosted by Harlow Gem Vault
Bring your best car(s) and join us to enjoy the party with sommelier selected wines, the best classic and modern cars and hors d'oeuvre catered by Penrose's Clam House. Live DJ.
August 26th 3-6 p.m.
This event is gratis.
RSVP to dana@birchwellmotors.example for address and details

Target Market(s)
Very wealthy exotic car owners
Industry/Entity Type
Car Club, Fine Wines.
Requirements
Must have
- Style, panache, elegance, sleekness, simplicity. I like the idea of a black or dark flyer with a consistent color scheme.
Nice to have
- I want the flyer to be simple and sleek, feature an Corvane Lestrel R7 as the eye catcher, Birchwell Motor Society logo featured prominently on the top, and the other business logos on the bottom.
Should not have
- It must not be too noisy or busy.

```html
<!DOCTYPE html>
<html lang="en">
<head>
<meta charset="utf-8">
<title>Fast Cars and Fine Wine – Birchwell Motor Society</title>
<link rel="stylesheet" href="https://fonts.googleapis.com/css2?family=Poiret+One&family=PT+Sans+Narrow:wght@400;700&display=swap">
<style>
  :root {
    --sky-light: #e4e4e2;
    --sky-mid: #bdbdbb;
    --ridge: #6e6e6e;
    --night: #2d2d2d;
    --night-deep: #1f1f1f;
    --ink: #1c1c1c;
    --paper: #ffffff;
    --soft: #d6d6d6;
    --bar: #9a9a9a;
    --floor: #bcbcbc;
    --car-red: #9a1c1c;
    --display: "Poiret One", sans-serif;
    --text: "PT Sans Narrow", sans-serif;
  }
  html, body { margin: 0; padding: 0; overflow: hidden; background: var(--night-deep); }
  .flyer {
    position: relative;
    width: 848px;
    height: 1200px;
    overflow: hidden;
    font-family: var(--text);
    color: var(--paper);
    background: linear-gradient(180deg, var(--night) 0%, var(--night) 60%, var(--night-deep) 100%);
  }
  .landscape {
    position: absolute; left: 0; top: 0; width: 848px; height: 470px;
    background:
      radial-gradient(ellipse 160px 110px at 700px 360px, rgba(255,255,255,0.9), rgba(255,255,255,0) 70%),
      linear-gradient(180deg, var(--sky-light) 0%, var(--sky-mid) 45%, var(--ridge) 72%, var(--night) 100%);
  }
  .club-name {
    position: absolute; left: 0; top: 120px; width: 848px;
    text-align: center; color: var(--ink); font-family: var(--text); font-weight: 700;
    text-transform: uppercase; line-height: 1;
  }
  .club-name .lead { display: block; font-size: 78px; letter-spacing: 6px; }
  .club-name .sub { display: block; font-size: 34px; letter-spacing: 14px; margin-top: 10px; }
  .rule {
    position: absolute; left: 97px; top: 432px; width: 331px; height: 7px;
    background: linear-gradient(90deg, var(--bar), rgba(154,154,154,0.2));
  }
  .presents { position: absolute; left: 97px; top: 458px; font-size: 14px; }
  .headline {
    position: absolute; left: 94px; top: 484px; margin: 0;
    font-family: var(--display); font-weight: 400; font-size: 74px; line-height: 78px;
    letter-spacing: 2px; text-transform: uppercase;
  }
  .aside {
    position: absolute; left: 546px; top: 573px; font-size: 23px; line-height: 24px; color: var(--paper);
  }
  .details { position: absolute; left: 97px; top: 652px; width: 335px; }
  .details .host { font-size: 14px; margin: 0 0 4px; }
  .details .body { font-size: 20px; line-height: 24px; margin: 0; }
  .when {
    position: absolute; left: 446px; top: 660px; width: 345px; height: 81px;
    background: linear-gradient(90deg, rgba(150,150,150,0.85), rgba(110,110,110,0.35) 70%, rgba(60,60,60,0));
    padding: 6px 0 0 16px; box-sizing: border-box;
  }
  .when .date { font-size: 30px; font-weight: 700; margin: 0; line-height: 38px; }
  .when .cost { font-size: 13px; margin: 8px 0 0; }
  .rsvp { position: absolute; left: 459px; top: 757px; }
  .rsvp .label { font-size: 14px; margin: 0; }
  .rsvp .email { font-size: 21px; margin: 10px 0 0; line-height: 22px; }
  .rsvp .note { font-size: 13px; margin: 0; }
  .car-photo {
    position: absolute; left: 290px; top: 830px; width: 558px; height: 232px;
    background:
      radial-gradient(ellipse 230px 80px at 300px 130px, rgba(170,40,40,0.95), rgba(120,25,25,0.6) 55%, rgba(60,60,60,0) 100%),
      radial-gradient(ellipse 300px 120px at 290px 170px, rgba(110,110,110,0.5), rgba(45,45,45,0) 100%);
  }
  .floor {
    position: absolute; left: 0; top: 1058px; width: 848px; height: 9px;
    background: linear-gradient(90deg, rgba(188,188,188,0.4), var(--floor) 50%, rgba(188,188,188,0.4));
  }
  .partners {
    position: absolute; left: 0; top: 1067px; width: 848px; height: 133px;
    background: var(--night-deep);
    display: flex; justify-content: center; align-items: center; gap: 70px;
  }
  .partner { display: flex; align-items: center; gap: 10px; font-size: 20px; color: var(--soft); }
  .partner .mark { width: 12px; height: 12px; background: var(--soft); }
</style>
</head>
<body>
<main class="flyer">
  <div class="landscape" role="img" aria-label="Grey mountain range under a rising sun with radiating light rays"></div>

  <h1 class="club-name"><span class="lead">Birchwell</span><span class="sub">Motor Society</span></h1>

  <div class="rule"></div>
  <p class="presents" style="margin:0">Birchwell Motor society presents</p>

  <h2 class="headline">Fast Cars and<br>Fine Wine</h2>
  <p class="aside" style="margin:0">but not while<br>driving</p>

  <section class="details">
    <p class="host">Hosted by Harlow Gem Vault</p>
    <p class="body">Bring your best car(s) and join us to enjoy the party with sommelier selected wines, the best classic and modern cars and hors d’oeuvre catered by Penrose’s Clam House. Live DJ.</p>
  </section>

  <section class="when">
    <p class="date">August 26th 3-6 p.m.</p>
    <p class="cost">This event is gratis.</p>
  </section>

  <section class="rsvp">
    <p class="label">RSVP to :</p>
    <p class="email">dana@birchwellmotors.example</p>
    <p class="note">for address and details</p>
  </section>

  <div class="car-photo" role="img" aria-label="Red Corvane Lestrel R7 classic sports car under a soft spotlight"></div>
  <div class="floor"></div>

  <footer class="partners">
    <div class="partner"><span class="mark"></span>Ferncliff Store</div>
    <div class="partner"><span class="mark"></span>Harlow Gem Vault</div>
  </footer>
</main>
</body>
</html>
```